Quillby Housecrafters Door Hanger design, Postcard and presentation folders Design

we are a home improvement company in Portland Oregon, are main service is roofing but we also do gutters, painting and pressure washing. we are a certified roofing contractor for TRV. We have over 20years of experince in the roofing industry we use top quality materials. Our mission is to do quality work and provide the best service.
Updates

This door hangers are going to be share to homeowners where we are currently working at! I will like to have a square maybe 2 inch wide and 1 inch hide (blank) for me to put the address where we are working at. So we want to give a direct message to homeowners who we are and why we are there for. Our services are roofing, gutters, painting, and pressure washing. But 95% of the door hangers should give the message that we are a roofing contractor. We are also certified by TRV which means all of our new roof projects have a 50 year warranty which only 2% of roofing contractor can offer that. We also offer finance, and all quality work. I will like to add photos of our trucks since all of them are wrap which will build them trust.

Target Market(s)

This door hangers should be custom for Homeowners with residential Homes,,, Average customer are between 40 & 65 Years old.

Industry/Entity Type

Roofing

Contact Information for Business Card

Logo, name, phone number, credentials, and services like roofing gutters painting and pressure washing

Font styles to use
Serif
Sans Serif
Decorative

Colors
33b8a4
5c5c5c

Requirements
Must have
• I want tho have a folder design just like this business card sample i uploaded. Teal and charcoal with services ...
Nice to have
• company trucks, job photo, crew photo and credential photos
Should not have
• I dont want it too busy or crowded..

```html
<!DOCTYPE html>
<html lang="en">
<head>
<meta charset="utf-8">
<title>Quillby Housecrafters Door Hanger</title>
<link rel="stylesheet" href="https://fonts.googleapis.com/css2?family=Roboto:wght@300;400;700;900&display=swap">
<style>
  :root {
    --backdrop: #ececec;
    --hole: #8c8c8c;
    --paper: #ffffff;
    --teal: #33b8a4;
    --teal-deep: #23917f;
    --charcoal: #5c5c5c;
    --charcoal-soft: #7a7a7a;
    --roof-dark: #3c4250;
    --siding: #6f6c5e;
  }
  * { margin: 0; padding: 0; box-sizing: border-box; }
  html, body {
    width: 1200px; height: 1000px; overflow: hidden;
    background: var(--backdrop);
    font-family: "Roboto", "Helvetica Neue", Arial, sans-serif;
  }
  .door-hanger {
    position: absolute; left: 462px; top: 97px;
    width: 302px; height: 753px;
    background: var(--paper);
    overflow: hidden;
  }
  .hang-hole {
    position: absolute; left: 105px; top: 33px;
    width: 92px; height: 92px; border-radius: 50%;
    background: var(--hole);
  }
  .company-name {
    position: absolute; top: 136px; width: 100%;
    text-align: center; color: var(--charcoal);
    font-weight: 700; font-size: 12px; letter-spacing: 1.6px;
  }
  .eyebrow {
    position: absolute; top: 160px; width: 100%;
    text-align: center; color: var(--teal);
    font-weight: 300; font-size: 13px; letter-spacing: 0.6px;
  }
  .headline {
    position: absolute; top: 174px; width: 100%;
    text-align: center; color: var(--teal);
    font-weight: 900; font-size: 56px; letter-spacing: 2px; line-height: 1;
  }
  .credential {
    position: absolute; top: 229px; width: 100%;
    text-align: center; color: var(--charcoal-soft);
    font-weight: 300; font-size: 11.5px; letter-spacing: 0.7px;
  }
  .credential strong { font-weight: 700; color: var(--teal); }
  .experience-band {
    position: absolute; top: 266px; left: 0; width: 100%; height: 42px;
    border-top: 3px solid var(--teal); border-bottom: 3px solid var(--teal);
    display: flex; align-items: center; justify-content: center;
    color: var(--charcoal); font-weight: 300; font-size: 16px; letter-spacing: 0.6px;
  }
  .experience-band strong { font-weight: 700; margin: 0 5px; color: var(--teal); }
  .mission {
    position: absolute; top: 325px; width: 100%;
    text-align: center; color: var(--teal);
    font-weight: 700; font-size: 13.5px; line-height: 16px; letter-spacing: 0.5px;
  }
  .warranty {
    position: absolute; top: 378px; width: 100%;
    text-align: center; color: var(--charcoal);
    font-weight: 700; font-size: 10.5px; letter-spacing: 0.5px;
  }
  .services {
    position: absolute; top: 396px; left: 19px;
    color: var(--charcoal-soft); font-weight: 300; font-size: 10.5px;
    line-height: 16px; letter-spacing: 0.5px; list-style: none;
  }
  .services li.item { padding-left: 10px; }
  .job-photo {
    position: absolute; top: 464px; left: 0; width: 100%; height: 289px;
    background: linear-gradient(180deg, #4a5060 0%, var(--roof-dark) 22%, var(--siding) 45%, #4d5060 62%, var(--roof-dark) 78%, #5b6150 100%);
  }
  .address-box {
    position: absolute; top: 566px; left: 71px;
    width: 160px; height: 80px;
    background: var(--paper);
    border: 2px solid var(--teal);
  }
  .call-band {
    position: absolute; top: 669px; left: 0; width: 100%; height: 38px;
    background: var(--paper);
    border-top: 3px solid var(--teal); border-bottom: 3px solid var(--teal);
    display: flex; align-items: center; justify-content: center;
    color: var(--teal-deep); font-size: 22px; letter-spacing: 0.3px;
  }
  .call-band strong { font-weight: 900; margin-right: 7px; }
  .call-band span { font-weight: 400; }
  .website {
    position: absolute; top: 721px; width: 100%;
    text-align: center; color: var(--paper);
    font-weight: 400; font-size: 15px;
  }
</style>
</head>
<body>
  <div class="door-hanger">
    <div class="hang-hole"></div>
    <p class="company-name">QUILLBY HOUSECRAFTERS</p>
    <p class="eyebrow">HOME IMPROVEMENT</p>
    <h1 class="headline">ROOFING</h1>
    <p class="credential">A CERTIFIED ROOFING CONTRACTOR FOR <strong>TRV</strong></p>
    <div class="experience-band">OVER <strong>20 YEARS</strong> OF EXPERIENCE</div>
    <p class="mission">OUR MISSION IS TO DO<br>QUALITY WORK AND PROVIDE<br>THE BEST SERVICE</p>
    <p class="warranty">50-YEAR WARRANTY ON EVERY NEW ROOF</p>
    <ul class="services">
      <li>OUR MAIN SERVICE IS ROOFING BUT WE ALSO DO</li>
      <li class="item">- GUTTERS</li>
      <li class="item">- PAINTING</li>
      <li class="item">- PRESSURE WASHING</li>
    </ul>
    <div class="job-photo" role="img" aria-label="Photo of a two-storey house with a newly installed dark shingle roof"></div>
    <div class="address-box" aria-label="Blank space for the job site address"></div>
    <div class="call-band"><strong>CALL US</strong><span>800-000-000</span></div>
    <p class="website">www.yourwebsite.com</p>
  </div>
</body>
</html>
```